SkyvoraQ Business Cards and Stationary Design

Need a design for our business cards and stationary. I want to carry on the theme of the logo. I want the business cards to have a design on the back. I would like the business cards and the stationary to carry the same theme, design scheme, and branding

Target Market(s)

Airlines and Maintenance Facilities

Industry/Entity Type

Aviation

Contact Information for Business Card

Name
Position Title
Address: 4827 Tollbeck Lane, Fort Pierce, Florida, 34951
Office Number
Mobile Number
Email
Website

Font styles to use
Serif
Sans Serif

Colors

Designer to choose colors to be used in the design.

```html
<!DOCTYPE html>
<html lang="en">
<head>
<meta charset="utf-8">
<title>SkyvoraQ Business Card</title>
<link rel="stylesheet" href="https://fonts.googleapis.com/css2?family=PT+Sans:wght@400;700&family=PT+Sans+Narrow:wght@700&display=swap">
<style>
  :root {
    --page: #e9ebee;
    --card: #ffffff;
    --navy: #0b2a52;
    --blue: #1e5fb3;
    --sky: #2aa5e8;
    --ink: #3a3f47;
    --white: #ffffff;
  }
  * { box-sizing: border-box; margin: 0; padding: 0; }
  html, body { width: 1200px; height: 872px; overflow: hidden; }
  body {
    background: var(--page);
    font-family: "PT Sans", Arial, sans-serif;
    display: flex;
    flex-direction: column;
    align-items: center;
    justify-content: center;
    gap: 40px;
  }
  .card {
    position: relative;
    width: 640px;
    height: 366px;
    background: var(--card);
    box-shadow: 0 6px 22px rgba(11, 42, 82, 0.18);
    overflow: hidden;
  }

  /* Back face */
  .card-back .brand-mark {
    position: absolute;
    left: 60px;
    top: 93px;
    width: 180px;
    height: 180px;
    border: 10px solid var(--blue);
    border-radius: 50%;
  }
  .card-back .brand-block {
    position: absolute;
    left: 280px;
    top: 148px;
  }
  .card-back .brand-name {
    font-weight: 700;
    font-size: 40px;
    letter-spacing: 6px;
    color: var(--navy);
    line-height: 1;
  }
  .card-back .brand-site {
    margin-top: 10px;
    margin-left: 60px;
    font-size: 15px;
    letter-spacing: 3px;
    color: var(--ink);
  }

  /* Front face */
  .card-front .band {
    position: absolute;
    inset: 0;
  }
  .card-front .brand-mark {
    position: absolute;
    left: 100px;
    top: 34px;
    width: 70px;
    height: 70px;
    border: 6px solid var(--blue);
    border-radius: 50%;
  }
  .card-front .brand-name {
    position: absolute;
    left: 48px;
    top: 118px;
    font-weight: 700;
    font-size: 40px;
    letter-spacing: 7px;
    color: var(--navy);
    line-height: 1;
  }
  .card-front .holder {
    position: absolute;
    left: 50px;
    top: 196px;
    color: var(--navy);
    font-size: 22px;
  }
  .holder .holder-name {
    font-family: "PT Sans Narrow", "Arial Narrow", sans-serif;
    font-weight: 700;
    font-size: 24px;
  }
  .holder .holder-title { font-size: 19px; }
  .contact {
    position: absolute;
    left: 50px;
    top: 262px;
    list-style: none;
    color: var(--white);
    font-size: 14.5px;
  }
  .contact li {
    display: flex;
    align-items: center;
    gap: 7px;
    height: 30px;
  }
  .contact .pair { margin-left: 12px; display: inline-flex; align-items: center; gap: 7px; }
  .icon { width: 15px; height: 15px; flex: none; }
</style>
</head>
<body>

  <section class="card card-back" aria-label="Business card back">
    <div class="brand-mark" aria-hidden="true"></div>
    <div class="brand-block">
      <p class="brand-name">SKYVORAQ</p>
      <p class="brand-site">www.skyvoraq.com</p>
    </div>
  </section>

  <section class="card card-front" aria-label="Business card front">
    <svg class="band" viewBox="0 0 640 366" aria-hidden="true">
      <defs>
        <linearGradient id="tab-fill" x1="0" y1="0" x2="1" y2="0">
          <stop offset="0" stop-color="#2aa5e8"/>
          <stop offset="1" stop-color="#1e4fa0"/>
        </linearGradient>
      </defs>
      <path d="M0,244 H438 Q462,244 476,262 L552,366 H0 Z" fill="#0b2a52"/>
      <path d="M578,222 H640 V366 H614 L552,268 Q536,234 578,222 Z" fill="url(#tab-fill)"/>
    </svg>

    <div class="brand-mark" aria-hidden="true"></div>
    <p class="brand-name">SKYVORAQ</p>

    <p class="holder"><span class="holder-name">MARCUS DELVANE,</span> <span class="holder-title">PRESIDENT</span></p>

    <ul class="contact">
      <li>
        <svg class="icon" viewBox="0 0 16 16" aria-hidden="true"><circle cx="8" cy="8" r="7" fill="none" stroke="#fff" stroke-width="1.3"/><path d="M5.5 4.5 L7 4.3 L7.5 6.3 L6.6 7 Q7.4 8.8 9 9.4 L9.7 8.5 L11.7 9 L11.5 10.5 Q8 11 5.5 7.5 Z" fill="#fff"/></svg>
        014-372-5810
        <span class="pair">
          <svg class="icon" viewBox="0 0 16 16" aria-hidden="true"><circle cx="8" cy="8" r="7" fill="none" stroke="#fff" stroke-width="1.3"/><rect x="5.5" y="4" width="5" height="8" rx="1" fill="none" stroke="#fff" stroke-width="1.2"/></svg>
          014-372-5810
        </span>
      </li>
      <li>
        <svg class="icon" viewBox="0 0 16 16" aria-hidden="true"><circle cx="8" cy="8" r="7" fill="none" stroke="#fff" stroke-width="1.3"/><rect x="4.3" y="5.3" width="7.4" height="5.4" fill="none" stroke="#fff" stroke-width="1.1"/><path d="M4.3 5.3 L8 8.3 L11.7 5.3" fill="none" stroke="#fff" stroke-width="1.1"/></svg>
        info@skyvoraq.com
        <span class="pair">
          <svg class="icon" viewBox="0 0 16 16" aria-hidden="true"><circle cx="8" cy="8" r="7" fill="none" stroke="#fff" stroke-width="1.3"/><ellipse cx="8" cy="8" rx="3" ry="7" fill="none" stroke="#fff" stroke-width="1.1"/><path d="M1 8 H15 M2.5 4.5 H13.5 M2.5 11.5 H13.5" stroke="#fff" stroke-width="1.1"/></svg>
          www.skyvoraq.com
        </span>
      </li>
      <li>
        <svg class="icon" viewBox="0 0 16 16" aria-hidden="true"><circle cx="8" cy="8" r="7" fill="none" stroke="#fff" stroke-width="1.3"/><path d="M8 12.5 Q4.8 8.6 4.8 6.9 A3.2 3.2 0 0 1 11.2 6.9 Q11.2 8.6 8 12.5 Z" fill="none" stroke="#fff" stroke-width="1.1"/><circle cx="8" cy="6.9" r="1.1" fill="#fff"/></svg>
        4827 Tollbeck Lane, Fort Pierce, Florida, 34951
      </li>
    </ul>
  </section>

</body>
</html>
```